Add Responsiveness to Current Website

The website http://www.quillbrook-sound-rooms.example needs to be made responsive. This includes all the menus and all the galleries. The Design, graphics, colors can remain the same, except I can provide larger images and design for the Home Page. If you know what you are doing, this should not take too long.

Coding

Coded - Design and coding required

Number of Pages Required

5+ page

Font styles to use
Sans Serif

Colors
f37122
f78f20

Requirements
Must have
• Responsive Menus and Galleries

```html
<!DOCTYPE html>
<html lang="en">
<head>
<meta charset="utf-8">
<title>Quillbrook – Home Theatre Arts &amp; Design</title>
<link href="https://fonts.googleapis.com/css2?family=Ubuntu:wght@400;500&display=swap" rel="stylesheet">
<style>
:root{
  --orange:#f37122;
  --orange-light:#f78f20;
  --text:#3a3a3a;
  --muted:#555;
  --white:#fff;
  --rule:#e4e4e4;
  --logo-olive:#6b6a2a;
}
*{margin:0;padding:0;box-sizing:border-box}
html,body{width:1200px;height:2889px;overflow:hidden}
body{position:relative;background:var(--white);font-family:"Ubuntu",sans-serif;color:var(--text)}
.abs{position:absolute}

/* header */
.site-header{left:0;top:0;width:1200px;height:100px;background:var(--white)}
.brand{left:115px;top:24px;display:flex;align-items:center;gap:10px;font-size:30px;font-weight:500;color:var(--logo-olive)}
.brand-mark{width:16px;height:16px;background:var(--logo-olive)}
.call{right:116px;top:28px;display:flex;align-items:center;gap:8px;font-size:13px;color:var(--orange)}
.main-nav{right:116px;top:56px;display:flex;gap:31px;font-size:12px;color:#333}

/* hero */
.hero{left:0;top:100px;width:1200px;height:503px;background:radial-gradient(ellipse at 50% 20%,#5a78d8 0%,#20306e 40%,#0c1030 75%,#2a0c1a 100%)}
.hero-title{left:0;top:334px;width:1200px;text-align:center;font-size:35px;color:var(--white)}
.hero-dots{left:559px;top:559px;display:flex;gap:8px}
.hero-dots span{width:9px;height:9px;border-radius:50%;background:var(--white)}
.hero-dots span.active{background:var(--orange)}

/* provide */
.section-title{left:0;top:652px;width:1200px;text-align:center;font-size:38px;color:var(--orange)}
.feature-img{width:343px;height:212px}
.feature{width:606px}
.feature h3{font-size:19px;font-weight:400;color:var(--orange);margin-bottom:14px}
.feature p{font-size:11.3px;line-height:16.5px;color:var(--muted);margin-bottom:15px}

/* gallery */
.gallery{left:0;top:1997px;width:1200px;height:563px;background:linear-gradient(180deg,#2c3440 0%,#1d1f24 55%,#121316 100%)}
.gallery-title{left:0;top:2037px;width:1200px;text-align:center;font-size:35px;color:var(--white)}
.slide{left:231px;top:2107px;width:738px;height:406px;background:linear-gradient(90deg,#d9dcdf 0%,#b7bcc0 35%,#c8392a 55%,#b8301f 75%,#3c3c3e 100%)}
.slide-caption{left:231px;top:2442px;width:738px;height:71px;background:rgba(30,30,30,.72);color:var(--white);font-size:14px;padding:28px 32px}
.slide-arrows{left:910px;top:2468px;display:flex;gap:14px}

/* footer */
.footer-col{top:2625px}
.footer-col h4{font-size:11px;font-weight:500;color:#222;margin-bottom:24px}
.footer-col li{list-style:none;font-size:11px;color:#333;line-height:25px}
.footer-col.social li{line-height:39px}
.footer-rule{left:0;top:2835px;width:1200px;height:1px;background:var(--rule)}
.copyright{left:0;top:2860px;width:1200px;text-align:center;font-size:11px;color:#333}
.footer-tag{right:43px;top:2860px;font-size:11px;color:#333}
</style>
</head>
<body>

<header class="site-header abs">
  <div class="brand abs"><span class="brand-mark"></span>Quillbrook</div>
  <div class="call abs">
    <svg width="13" height="13" viewBox="0 0 24 24"><path fill="#f37122" d="M6.6 10.8a15 15 0 0 0 6.6 6.6l2.2-2.2a1 1 0 0 1 1-.25 11.4 11.4 0 0 0 3.6.57 1 1 0 0 1 1 1V20a1 1 0 0 1-1 1A17 17 0 0 1 3 4a1 1 0 0 1 1-1h3.5a1 1 0 0 1 1 1c0 1.25.2 2.45.57 3.6a1 1 0 0 1-.25 1z"/></svg>
    Call Today (555-014-2290)
  </div>
  <nav class="main-nav abs">
    <span>Home</span><span>Products</span><span>Gallery</span><span>Let's Begin</span><span>Acoustics</span><span>Our Story</span><span>Hospitality</span><span>Seating</span><span>Contact</span>
  </nav>
</header>

<section class="hero abs" role="img" aria-label="Dark home theatre with rows of blue leather recliners under a ceiling light"></section>
<h1 class="hero-title abs" style="font-weight:400">Home Theatre Arts &amp; Design</h1>
<div class="hero-dots abs"><span class="active"></span><span></span><span></span><span></span><span></span></div>

<h2 class="section-title abs" style="font-weight:400">What We Provide</h2>

<div class="feature-img abs" style="left:115px;top:745px;background:linear-gradient(135deg,#7a3a22,#c07a3a 55%,#d9b77a)" role="img" aria-label="Home theatre room with beige recliners and red walls"></div>
<article class="feature abs" style="left:476px;top:766px">
  <h3>Home Theater Design</h3>
  <p>In terms of design, your Home Theater is the most versatile room in your home. Your options are limitless. You can compliment your existing home decor or you can create a design that is completely different from the rest of your home.If you enjoy exploring unique design opportunities, our decorative acoustic panels can act as a canvas for your inspiration. Marcus Ellery created dozens of original artistic designs specifically for Home Theater Interiors.</p>
  <p>Perhaps, you perfer a theme for your Home Theater Design. If so, we have designed theaters devoted to Outer Space, Wine, Sports, Music, Skylines, Spy Thriller, Red Woods (and other landscapes) and more.Call Marcus today to discuss any of your Home Theater or Acoustic Panel needs and ask about our complimentary rendering services.</p>
</article>

<article class="feature abs" style="left:115px;top:1057px">
  <h3>Your Personal Consultant</h3>
  <p>In terms of design, your Home Theater is the most versatile room in your home. Your options are limitless. You can compliment your existing home decor or you can create a design that is completely different from the rest of your home.If you enjoy exploring unique design opportunities, our decorative acoustic panels can act as a canvas for your inspiration. Marcus Ellery created dozens of original artistic designs specifically for Home Theater Interiors.</p>
  <p>Perhaps, you perfer a theme for your Home Theater Design. If so, we have designed theaters devoted to Outer Space, Wine, Sports, Music, Skylines, Spy Thriller, Red Woods (and other landscapes) and more.Call Marcus today to discuss any of your Home Theater or Acoustic Panel needs and ask about our complimentary rendering services.</p>
</article>
<div class="feature-img abs" style="left:740px;top:1038px;background:linear-gradient(180deg,#d8d8d8,#9a9a9a 50%,#3a3a3a)" role="img" aria-label="Black tower speakers around an audio amplifier"></div>

<div class="feature-img abs" style="left:115px;top:1356px;background:linear-gradient(180deg,#1a1a1a,#5a4a3c 55%,#d8d2c6)" role="img" aria-label="Dark theatre with cream recliners facing a screen"></div>
<article class="feature abs" style="left:476px;top:1375px">
  <h3>Custom Panels and Designs</h3>
  <p>In terms of design, your Home Theater is the most versatile room in your home. Your options are limitless. You can compliment your existing home decor or you can create a design that is completely different from the rest of your home.If you enjoy exploring unique design opportunities, our decorative acoustic panels can act as a canvas for your inspiration. Marcus Ellery created dozens of original artistic designs specifically for Home Theater Interiors.</p>
  <p>Perhaps, you perfer a theme for your Home Theater Design. If so, we have designed theaters devoted to Outer Space, Wine, Sports, Music, Skylines, Spy Thriller, Red Woods (and other landscapes) and more.Call Marcus today to discuss any of your Home Theater or Acoustic Panel needs and ask about our complimentary rendering services.</p>
</article>

<article class="feature abs" style="left:115px;top:1700px">
  <h3>Featured Home Movie Theater Products</h3>
  <p>In terms of design, your Home Theater is the most versatile room in your home. Your options are limitless. You can compliment your existing home decor or you can create a design that is completely different from the rest of your home.If you enjoy exploring unique design opportunities, our decorative acoustic panels can act as a canvas for your inspiration. Marcus Ellery created dozens of original artistic designs specifically for Home Theater Interiors.</p>
  <p>Perhaps, you perfer a theme for your Home Theater Design. If so, we have designed theaters devoted to Outer Space, Wine, Sports, Music, Skylines, Spy Thriller, Red Woods (and other landscapes) and more.Call Marcus today to discuss any of your Home Theater or Acoustic Panel needs and ask about our complimentary rendering services.</p>
</article>
<div class="feature-img abs" style="left:740px;top:1680px;background:linear-gradient(180deg,#eeeeee,#c9c9c9 50%,#7a4a2a)" role="img" aria-label="Bright living room with wall-mounted TV and wooden floor"></div>

<section class="gallery abs" role="img" aria-label="Dark home theatre interior with leather seating"></section>
<h2 class="gallery-title abs" style="font-weight:400">Photo Gallery</h2>
<div class="slide abs" role="img" aria-label="Modern lounge with red feature wall, grey sofa and wall TV"></div>
<div class="slide-caption abs">Neque porro quisquam est qui dolorem ipsum quia dolor sit amet</div>
<div class="slide-arrows abs">
  <svg width="12" height="18" viewBox="0 0 12 18"><path d="M10 2 3 9l7 7" fill="none" stroke="#f37122" stroke-width="2.5"/></svg>
  <svg width="12" height="18" viewBox="0 0 12 18"><path d="m2 2 7 7-7 7" fill="none" stroke="#f37122" stroke-width="2.5"/></svg>
</div>

<footer>
  <div class="footer-col abs" style="left:115px"><h4>Company Info</h4><ul><li>Contact</li><li>Company History</li></ul></div>
  <div class="footer-col abs" style="left:343px"><h4>Designs</h4><ul><li>Artesian Panels</li><li>Themes</li><li>Universal Theme</li><li>Completed Projects</li><li>Custom Theaters</li><li>Conventional Fabrics</li></ul></div>
  <div class="footer-col abs" style="left:570px"><h4>Theater Seating</h4><ul><li>Theater Seating</li></ul></div>
  <div class="footer-col abs" style="left:765px"><h4>Information</h4><ul><li>Getting Started</li><li>Acoustics 101</li></ul></div>
  <div class="footer-col social abs" style="left:946px"><h4 style="margin-bottom:16px">Connect With Us</h4><ul><li>Friendbook</li><li>Chirper</li><li>Workfolio</li></ul></div>
  <div class="footer-rule abs"></div>
  <div class="copyright abs">© 2015 Company Name, All Rights Reserved</div>
  <div class="footer-tag abs">CS</div>
</footer>

</body>
</html>
```